Fairway Circuit web site

Fairway Circuit is a High End golf amateur Tour targeted to wealthy golf passionates.
The concept is to take average golfers and offer them the same playing conditions than the pros (Caddies, branded bags, TV coverage...) and bring them to the most beautiful golf courses around the world.
Keywords: International, Exclusive, Luxury, but not show-off...
The Task is to design the WordPress template and a exemple page.
Please use the provided logo and any stock image you like.
Updates

Hello,

please note that the outcome has to be a fully coded WordPress site.

Please no "Photoshop only" designs...

Thanks

```html
<!DOCTYPE html>
<html lang="en">
<head>
<meta charset="utf-8">
<title>Fairway Circuit</title>
<link rel="stylesheet" href="https://fonts.googleapis.com/css2?family=Open+Sans:wght@400;600;700&family=Arimo:wght@400;700&display=swap">
<style>
:root{
  --green:#6aa121;
  --green-bright:#7ec322;
  --green-deep:#0b4a2a;
  --nav:#1f5a2c;
  --ink:#2b2b2b;
  --muted:#8a8a8a;
  --band:#ebebeb;
  --footer:#262626;
  --footer-top:#3a3a3a;
  --bar:#2a2a1d;
  --blue:#3a7bd5;
  --white:#fff;
}
*{margin:0;padding:0;box-sizing:border-box}
html,body{width:802px;height:1200px;overflow:hidden;background:var(--white)}
body{position:relative;font-family:"Arimo",Arial,sans-serif;color:var(--ink)}
.abs{position:absolute}
.brand{left:26px;top:30px;display:flex;align-items:center;gap:8px}
.brand-dot{width:40px;height:40px;border-radius:50%;background:var(--green-deep)}
.brand-name{font-family:"Open Sans",sans-serif;font-weight:700;font-size:17px;color:var(--green-deep);line-height:1.1;width:90px}
.nav{top:72px;left:0;font-family:"Open Sans",sans-serif;font-size:14.5px;color:var(--nav)}
.nav a{position:absolute;white-space:nowrap;color:inherit;text-decoration:none}
.ribbon{left:670px;top:0;width:98px;height:125px;background:var(--green-deep);clip-path:polygon(0 0,100% 0,100% 100%,95% 97%,90% 100%,85% 97%,80% 100%,75% 97%,70% 100%,65% 97%,60% 100%,55% 97%,50% 100%,45% 97%,40% 100%,35% 97%,30% 100%,25% 97%,20% 100%,15% 97%,10% 100%,5% 97%,0 100%)}
.ribbon-bar{height:19px;background:#111;color:var(--white);font-family:"Open Sans",sans-serif;font-weight:700;font-size:11px;display:flex;align-items:center;justify-content:center;gap:12px}
.ribbon-name{margin:28px auto 0;width:80px;text-align:center;font-family:"Open Sans",sans-serif;font-weight:700;font-size:12px;color:var(--white);line-height:1.3}
.hero{left:18px;top:109px;width:768px;height:343px;border-radius:0 14px 0 0;overflow:hidden;background:linear-gradient(180deg,#4d5a2c 0%,#6f8a3a 40%,#7aa23e 70%,#5d8a2c 100%)}
.dots{left:16px;top:15px;display:flex;gap:4px}
.dots i{display:block;width:11px;height:4px;background:var(--white)}
.dots i.on{background:var(--blue)}
.enquiry{left:18px;top:286px;width:209px;height:104px;background:rgba(20,50,15,.85);border:1px solid #2e5b86;border-bottom:none}
.field{position:absolute;left:15px;height:20px;border:1px solid #d0d0d0;background:rgba(15,40,10,.6);color:var(--white);font-size:10.5px;padding-left:6px;display:flex;align-items:center;justify-content:space-between;padding-right:6px}
.send{position:absolute;left:16px;top:79px;color:var(--green-bright);font-family:"Open Sans",sans-serif;font-weight:700;font-size:12.5px;display:flex;gap:6px;align-items:center}
.bar{left:18px;top:390px;width:768px;height:62px;background:var(--bar);border-radius:0 0 0 14px}
.bar-item{position:absolute;top:17px;display:flex;align-items:center;gap:14px;color:var(--white);font-weight:700;font-size:9.5px;line-height:1.35}
.pitch{left:418px;top:362px;width:368px;height:90px;background:var(--bar);clip-path:polygon(22px 0,100% 0,100% 100%,0 100%)}
.pitch h3{position:absolute;left:24px;top:20px;color:var(--green-bright);font-family:"Open Sans",sans-serif;font-size:16px;font-weight:700}
.pitch p{position:absolute;left:23px;top:46px;width:330px;color:var(--white);font-size:9.5px;line-height:1.45}
.hero-shade{left:18px;top:452px;width:768px;height:26px;background:linear-gradient(#e4e4e4,#fff)}
.rule{left:30px;top:499px;width:742px;height:1px;background:#eee}
.intro{left:30px;top:512px;width:742px;text-align:center;font-family:"Open Sans",sans-serif;font-size:13.5px;line-height:20px;color:var(--ink)}
.intro b{color:var(--green);font-weight:600}
.rule-full{left:0;top:579px;width:802px;height:1px;background:#ddd}
.card{position:absolute;top:612px;width:163px}
.card-pic{height:93px;border-radius:3px;position:relative;overflow:hidden}
.card-pic span{position:absolute;left:0;bottom:0;width:100%;height:25px;background:rgba(40,30,20,.55);color:var(--green-bright);font-family:"Open Sans",sans-serif;font-size:11.5px;padding:5px 8px}
.card p{margin:19px 8px 0;font-size:9.3px;line-height:13.8px;color:var(--muted)}
.band{left:0;top:802px;width:802px;height:67px;background:var(--band)}
.ico{position:absolute;top:20px;width:24px;height:24px;border:1px solid #cfcfcf;border-radius:4px;background:var(--white)}
.ico svg{display:block;margin:4px auto}
.soc{position:absolute;top:20px;width:24px;height:24px;border-radius:4px;background:var(--blue)}
.footer{left:0;top:869px;width:802px;height:331px;background:var(--footer);border-top:6px solid var(--footer-top)}
.fh{position:absolute;top:34px;color:var(--green);font-family:"Open Sans",sans-serif;font-weight:700;font-size:13px}
.news{position:absolute;left:23px;width:250px;height:51px}
.news .th{position:absolute;left:0;top:0;width:51px;height:51px;border:1px solid #ddd}
.news h4{position:absolute;left:64px;top:2px;color:var(--green-bright);font-family:"Open Sans",sans-serif;font-weight:600;font-size:12px;white-space:nowrap}
.news p{position:absolute;left:64px;top:22px;width:190px;color:#e6e6e6;font-size:9.3px;line-height:14px}
.tweet{position:absolute;left:292px;width:181px;font-size:10.5px;line-height:17px;color:var(--white)}
.tweet em{font-style:normal;color:var(--green-bright)}
.tweet a{color:var(--green-bright);text-decoration:none;display:block}
.tline{position:absolute;left:292px;width:181px;height:1px;background:#444}
.tile{position:absolute;width:55px;height:55px}
.copy{left:23px;top:296px;color:#ddd;font-size:10.5px}
.copy span{color:var(--green-bright)}
.foot-line{left:0;top:270px;width:802px;height:1px;background:#3c3c3c}
.flinks a{position:absolute;top:295px;color:var(--green-bright);font-size:10.5px;text-decoration:none;white-space:nowrap}
</style>
</head>
<body>

<header>
  <div class="abs brand"><div class="brand-dot"></div><div class="brand-name">Fairway Circuit</div></div>
  <nav class="abs nav">
    <a style="left:206px">Home</a><a style="left:285px">About</a><a style="left:355px">Services</a><a style="left:444px">Courses</a><a style="left:521px">Contact Us</a>
  </nav>
  <div class="abs ribbon">
    <div class="ribbon-bar">CONTACT <span>&#9662;</span></div>
    <div class="ribbon-name">Fairway Circuit</div>
  </div>
</header>

<section class="abs hero" role="img" aria-label="Gloved hand placing a golf ball on a green">
  <div class="abs dots"><i></i><i></i><i class="on"></i><i></i></div>
</section>

<form class="abs enquiry">
  <div class="field" style="top:16px;width:174px">Choose your Sport <span>&#9662;</span></div>
  <div class="field" style="top:45px;width:85px">Date
    <svg width="10" height="10" viewBox="0 0 10 10"><rect x=".5" y=".5" width="9" height="9" fill="none" stroke="#fff"/><path d="M0 3h10M3 3v7M6 3v7M0 6h10" stroke="#fff"/></svg></div>
  <div class="send"><svg width="11" height="11" viewBox="0 0 11 11"><rect x=".5" y="1.5" width="9" height="9" fill="none" stroke="#fff"/><path d="M3 5l2 2 5-6" stroke="#fff" fill="none" stroke-width="1.5"/></svg>SEND ENQUIRY</div>
</form>

<div class="abs bar">
  <div class="bar-item" style="left:14px"><svg width="30" height="30" viewBox="0 0 30 30"><rect width="30" height="30" rx="3" fill="#3a7bd5"/><path d="M10 8v16M10 9l10 3-10 3" stroke="#fff" stroke-width="2" fill="#fff"/></svg><span>SPORT<br>RESERVATION</span></div>
  <div class="bar-item" style="left:151px"><svg width="30" height="30" viewBox="0 0 30 30"><circle cx="13" cy="13" r="10" fill="none" stroke="#fff" stroke-width="2.5"/><path d="M20 20l8 8" stroke="#fff" stroke-width="3"/></svg><span>SPORT<br>RESERVATION</span></div>
  <div class="bar-item" style="left:286px"><svg width="30" height="30" viewBox="0 0 30 30"><rect x="2" y="5" width="22" height="22" fill="none" stroke="#fff" stroke-width="2"/><path d="M7 15l5 6 14-18" stroke="#fff" stroke-width="3" fill="none"/></svg><span>CUSTOM<br>SERVICES</span></div>
</div>

<div class="abs pitch">
  <h3>Pitch &amp; Put</h3>
  <p>Duis aute irure dolor reprehenderit in voluptate velit esse cillum dolore eu fugiat nulla pariatur. Excepteur sint occaecat cupidatat.</p>
</div>
<div class="abs hero-shade"></div>

<div class="abs rule"></div>
<p class="abs intro">Lorem ipsum dolor sit amet, <b>consectetur adipisicing elit</b>, sed do eiusmod tempor incididunt ut labore et dolore magna aliqua. Ut enim ad minim veniam, quis nostrud exercitation ullamco <b>laboris nisi</b> ut aliquip ex.</p>
<div class="abs rule-full"></div>

<section>
  <article class="card" style="left:30px"><div class="card-pic" role="img" aria-label="Tree-lined golf course fairway" style="background:linear-gradient(#4a6a2a,#7ea040 55%,#5a8a2a)"><span>Golf</span></div><p>Duis aute irure dolor reprehenderit in voluptate velit esse cillum dolore eu fugiat nulla pariatur. Excepteur sint occaecat cupidatat.</p></article>
  <article class="card" style="left:223px"><div class="card-pic" role="img" aria-label="Climber on an indoor climbing wall" style="background:linear-gradient(135deg,#b8a898,#8c7a6a 60%,#a39080)"><span>Indoor Climbing</span></div><p>Lorem ipsum dolor sit consectetur adipisicing elit amet sid do eiusmod tempor incididunt labore sint occaecat.</p></article>
  <article class="card" style="left:417px"><div class="card-pic" role="img" aria-label="Tennis player on a clay court" style="background:linear-gradient(135deg,#c8572a,#a8401c)"><span>Tennis</span></div><p>Duis aute irure dolor reprehenderit in voluptate velit esse cillum dolore eu fugiat nulla pariatur. Excepteur sint occaecat cupidatat.</p></article>
  <article class="card" style="left:610px"><div class="card-pic" role="img" aria-label="Warmly lit hotel bedroom" style="background:linear-gradient(135deg,#8a6a40,#4a3420 70%)"><span>Hotel Reservation</span></div><p>Duis aute irure dolor reprehenderit in voluptate velit esse cillum dolore eu fugiat nulla pariatur. Excepteur sint occaecat cupidatat.</p></article>
</section>

<section class="abs band">
  <div class="ico" style="left:103px"><svg width="14" height="14"><circle cx="7" cy="7" r="6" fill="none" stroke="#333" stroke-width="1.5"/></svg></div>
  <div class="ico" style="left:132px"><svg width="14" height="14"><path d="M4 1v12M10 1v12" stroke="#333" stroke-width="2"/></svg></div>
  <div class="ico" style="left:160px"><svg width="14" height="14"><rect x="2" y="6" width="10" height="5" fill="#333"/></svg></div>
  <div class="ico" style="left:189px"><svg width="14" height="14"><path d="M2 2l10 10M12 2L2 12" stroke="#333" stroke-width="2"/></svg></div>
  <div class="ico" style="left:217px"><svg width="14" height="14"><rect x="3" y="2" width="8" height="10" fill="none" stroke="#333" stroke-width="2"/></svg></div>
  <div class="ico" style="left:246px"><svg width="14" height="14"><path d="M5 1v7h6v5" stroke="#333" stroke-width="2" fill="none"/></svg></div>
  <div class="ico" style="left:274px"><svg width="14" height="14"><path d="M2 2h8v10H2zM2 12h11" stroke="#333" stroke-width="1.5" fill="none"/></svg></div>
  <div class="ico" style="left:317px"><svg width="14" height="14"><circle cx="7" cy="7" r="5" fill="none" stroke="#333" stroke-width="2"/><circle cx="7" cy="7" r="2" fill="#333"/></svg></div>
  <div class="ico" style="left:346px"><svg width="14" height="14"><path d="M9 2Q3 7 9 12" stroke="#333" stroke-width="2.5" fill="none"/></svg></div>
  <div class="ico" style="left:374px"><svg width="14" height="14"><path d="M2 2l10 10" stroke="#333" stroke-width="2"/><rect x="4" y="4" width="7" height="7" fill="none" stroke="#333"/></svg></div>
  <div class="ico" style="left:403px"><svg width="14" height="14"><rect x="2" y="2" width="10" height="9" fill="none" stroke="#333" stroke-width="2"/></svg></div>
  <div class="ico" style="left:431px"><svg width="14" height="14"><rect x="1" y="6" width="12" height="5" rx="2" fill="none" stroke="#333" stroke-width="1.5"/></svg></div>
  <div class="ico" style="left:460px"><svg width="14" height="14"><path d="M2 12L7 2l5 10z" fill="#333"/></svg></div>
  <div class="ico" style="left:503px"><svg width="14" height="14"><rect x="1" y="3" width="12" height="8" fill="#333"/></svg></div>
  <div class="ico" style="left:531px"><svg width="14" height="14"><rect x="1" y="3" width="12" height="8" fill="#333"/></svg></div>
  <div class="ico" style="left:559px"><svg width="14" height="14"><rect x="1" y="3" width="12" height="8" fill="#333"/></svg></div>
  <div class="ico" style="left:588px"><svg width="14" height="14"><rect x="1" y="3" width="12" height="8" fill="#333"/></svg></div>
  <div class="soc" style="left:631px"></div>
  <div class="soc" style="left:659px"></div>
  <div class="soc" style="left:688px"></div>
  <div class="soc" style="left:716px"></div>
  <div class="soc" style="left:745px"></div>
</section>

<footer class="abs footer">
  <h2 class="fh" style="left:23px">THE LATEST NEWS</h2>
  <h2 class="fh" style="left:292px">Latest Tweets</h2>
  <h2 class="fh" style="left:497px">SNAPSHOTS GALLERY</h2>

  <div class="news" style="top:61px"><div class="th" role="img" aria-label="Indoor climbing wall" style="background:linear-gradient(135deg,#c8c0b8,#7a6e66)"></div><h4>Indoor Climbing Tournament</h4><p>Lorem ipsum dolor amet laboris consectetur adipisicing elit,</p></div>
  <div class="news" style="top:124px"><div class="th" role="img" aria-label="Tennis player serving" style="background:linear-gradient(135deg,#3a5aa0,#8aa0c8)"></div><h4>Tennis Cup 2012</h4><p>Lorem ipsum dolor amet laboris consectetur adipisicing elit,</p></div>
  <div class="news" style="top:187px"><div class="th" role="img" aria-label="Golf ball on the green" style="background:linear-gradient(#9ab060,#4a7a20)"></div><h4>International Golf Cup</h4><p>Lorem ipsum dolor amet laboris consectetur adipisicing elit,</p></div>

  <div class="tweet" style="top:67px">10 #<em>Free</em> Mockup #<em>Backgrounds</em><a>http://fwc.li/7Rbq2Lm</a></div>
  <div class="tline" style="top:116px"></div>
  <div class="tweet" style="top:133px">#<em>Free</em> Simple #<em>Icons</em><a>http://fwc.li/4Ktz9Hd</a></div>
  <div class="tline" style="top:182px"></div>

  <div class="tile" role="img" aria-label="Golf ball close up" style="left:497px;top:60px;background:linear-gradient(#3a8a30,#1a4a10)"></div>
  <div class="tile" role="img" aria-label="Golf balls on tees" style="left:557px;top:60px;background:linear-gradient(#d8d8d0,#5a8a30)"></div>
  <div class="tile" role="img" aria-label="Club striking a ball" style="left:617px;top:60px;background:linear-gradient(#4a78b8,#4a8a30)"></div>
  <div class="tile" role="img" aria-label="Gloved hand with ball" style="left:497px;top:122px;background:linear-gradient(#e0e0d8,#5a7a30)"></div>
  <div class="tile" role="img" aria-label="Golfer on the fairway" style="left:557px;top:122px;background:linear-gradient(#3a80c8,#4a9a30)"></div>
  <div class="tile" role="img" aria-label="Golfer in warm light" style="left:617px;top:122px;background:linear-gradient(#c89a50,#6a4a20)"></div>
  <div class="tile" role="img" aria-label="Golfer swinging" style="left:497px;top:183px;background:linear-gradient(#6a8a50,#3a6a20)"></div>
  <div class="tile" role="img" aria-label="Golf ball at sunset" style="left:557px;top:183px;background:linear-gradient(#c8a040,#4a5a20)"></div>
  <div class="tile" role="img" aria-label="Club and ball on grass" style="left:617px;top:183px;background:linear-gradient(#e8e8e0,#7ab040)"></div>

  <div class="abs foot-line"></div>
  <p class="abs copy">© 2014 Copyright Fairway Circuit by . <span>All rights reserved.</span></p>
  <nav class="flinks"><a style="left:455px">Home</a><a style="left:502px">About</a><a style="left:546px">Play Golf</a><a style="left:611px">Indoor Climbing</a><a style="left:704px">Blog</a><a style="left:743px">Contact</a></nav>
</footer>

</body>
</html>
```